Business Cards

I'm an contractor and consultant in IT Project management. I'd like a design for business cards.
In my work I mostly meet clients, peer project managers and technical staff. I usually exchange business cards at technical conventions or when networking.
I provide services that are:
- Updated, always with a fresh look on technology
- Solid and reliable
- Flexible schedule and always available
The current business card has been attached to provide information.
Target Market(s)
IT managers, IT project managers, consultants, recruitment staff. Age 30-45 years. College/University degree.
Industry/Entity Type
Contractor
Colors
Designer to choose colors to be used in the design.
Requirements
Must have
- Two sides, one side with personal information and the other side with company name.
Text in Norwegian, including Norwegian characters
Nice to have
- It should be possible for non-Norwegian speakers to read the contact details.

```html
<!DOCTYPE html>
<html lang="no">
<head>
<meta charset="utf-8">
<title>Eirik Dahlø – Visittkort</title>
<link rel="stylesheet" href="https://fonts.googleapis.com/css2?family=Questrial&family=Michroma&family=Josefin+Sans:wght@600&display=swap">
<style>
  :root {
    --page-bg: #8e8e8e;
    --card-bg: #f4f4f4;
    --card-edge: #e2e2e2;
    --ink: #111111;
  }
  * { margin: 0; padding: 0; box-sizing: border-box; }
  html, body {
    width: 1200px;
    height: 1200px;
    overflow: hidden;
    background: var(--page-bg);
  }
  .canvas {
    width: 1200px;
    height: 1200px;
    display: flex;
    flex-direction: column;
    align-items: center;
    justify-content: center;
    gap: 60px;
  }
  .card {
    width: 860px;
    height: 500px;
    background: radial-gradient(circle at 45% 45%, #ffffff 0%, var(--card-bg) 60%, var(--card-edge) 100%);
    color: var(--ink);
    position: relative;
  }
  /* Front side */
  .card--front {
    display: flex;
    flex-direction: column;
    align-items: center;
    justify-content: center;
  }
  .brand {
    display: flex;
    align-items: center;
    gap: 16px;
    font-family: "Questrial", sans-serif;
    letter-spacing: 0.02em;
    color: var(--ink);
  }
  .brand__square {
    width: 18px;
    height: 18px;
    background: var(--ink);
  }
  .card--front .brand { font-size: 58px; }
  .card--front .title {
    margin-top: 22px;
    font-family: "Michroma", sans-serif;
    font-size: 17px;
    letter-spacing: 0.18em;
  }
  /* Back side */
  .card--back {
    display: flex;
    align-items: center;
  }
  .identity {
    width: 410px;
    padding-left: 70px;
  }
  .card--back .brand { font-size: 40px; gap: 12px; }
  .card--back .brand__square { width: 13px; height: 13px; }
  .identity__role {
    margin-top: 18px;
    font-family: "Michroma", sans-serif;
    font-size: 11px;
    letter-spacing: 0.12em;
  }
  .identity__company {
    margin-top: 14px;
    margin-left: 8px;
    font-family: "Questrial", sans-serif;
    font-size: 17px;
  }
  .divider {
    width: 2px;
    height: 250px;
    background: var(--ink);
  }
  .contact {
    list-style: none;
    padding-left: 40px;
    font-family: "Josefin Sans", sans-serif;
    font-weight: 600;
    font-size: 19px;
    line-height: 2.4;
  }
</style>
</head>
<body>
<main class="canvas">
  <section class="card card--front" aria-label="Forside">
    <div class="brand"><span class="brand__square"></span><span class="brand__name">EIRIK DAHLØ</span></div>
    <p class="title">IT RÅDGIVER</p>
  </section>

  <section class="card card--back" aria-label="Bakside">
    <div class="identity">
      <div class="brand"><span class="brand__square"></span><span class="brand__name">EIRIK DAHLØ</span></div>
      <p class="identity__role">IT RÅDGIVER, DAHLØ CONSULTING</p>
      <p class="identity__company">Dahlø Consulting</p>
    </div>
    <div class="divider"></div>
    <ul class="contact">
      <li>M: +47 91234567</li>
      <li>E: eirik@dahloconsulting.no</li>
      <li>L: http://www.profilnett.no/in/eirikdahlo</li>
      <li>A: Fjellveien 14, 0480 Oslo</li>
    </ul>
  </section>
</main>
</body>
</html>
```